Update Business Card Design Project

We've been in business nearly 15 years and about 10 years ago developed a brand that is now well recognized. The business card is boring, too much print and nothing that says 'We are TRULY MARVELOUS' right off the mark.
We are a fun store, lots of new things on a regular basis. Especially in kitchen goods where the colours are strong and the emphasis is on pretty and practical. We like to have both!
Updates
Hi there,
Target Market(s)
Store customers and suppliers
Demographics aged 40-70yrs, mid to high income, mostly women or couples, rural setting but in the 'shopping district' of our region. 1 hour to nearest city.
Industry/Entity Type
Business
Requirements
Nice to have
- Incorporate the logo, if possible

```html
<!DOCTYPE html>
<html lang="en">
<head>
<meta charset="utf-8">
<title>Truly Marvelous – Business Card</title>
<link href="https://fonts.googleapis.com/css2?family=Arimo:wght@400;700&display=swap" rel="stylesheet">
<style>
  :root {
    --stage: #ece9e4;
    --card: #ffffff;
    --ink: #2b2b2b;
    --orange: #f5a515;
    --sweep: #c9c9c9;
    --muted: #3a3a3a;
  }
  * { box-sizing: border-box; margin: 0; padding: 0; }
  html, body {
    width: 1158px; height: 1200px; overflow: hidden;
    background: var(--stage);
    font-family: "Arimo", Arial, sans-serif;
    color: var(--ink);
  }
  .card {
    position: absolute;
    width: 723px; height: 410px;
    background: var(--card);
    border-radius: 18px;
    overflow: hidden;
    box-shadow: 0 4px 14px rgba(0,0,0,0.12);
  }
  .card--front { left: 199px; top: 97px; }
  .card--back  { left: 208px; top: 658px; }

  .front-art { position: absolute; inset: 0; }

  .brand {
    position: absolute;
    display: flex; flex-direction: column; align-items: center;
    text-align: center;
  }
  .brand__mark {
    width: 22px; height: 22px;
    background: var(--ink);
    margin-bottom: 12px;
  }
  .brand__name {
    font-weight: 700;
    text-transform: uppercase;
    color: var(--ink);
    line-height: 1.15;
  }
  .card--front .brand { left: 18px; top: 148px; width: 200px; }
  .card--front .brand__name { font-size: 19px; letter-spacing: 2px; }
  .card--back .brand { left: 0; right: 0; top: 120px; }
  .card--back .brand__mark { width: 40px; height: 40px; margin-bottom: 22px; }
  .card--back .brand__name { font-size: 38px; letter-spacing: 4px; }

  .divider {
    position: absolute; left: 250px; top: 69px;
    width: 2px; height: 262px;
    background: var(--orange);
  }

  .person {
    position: absolute; left: 400px; top: 154px; width: 168px;
    text-align: center;
  }
  .person__name { font-size: 20px; font-weight: 700; color: var(--orange); }
  .person__role { font-size: 11px; color: var(--orange); margin-top: 2px; }

  .address {
    position: absolute; left: 290px; top: 204px;
    font-size: 13px; line-height: 19px; color: var(--muted);
  }

  .contacts {
    position: absolute; left: 283px; top: 261px;
    list-style: none;
    font-size: 13px; line-height: 17px; color: var(--muted);
  }
  .contacts li { display: flex; align-items: center; gap: 6px; }
  .contacts svg { width: 11px; height: 11px; flex: none; fill: var(--orange); }
</style>
</head>
<body>

<section class="card card--front">
  <svg class="front-art" viewBox="0 0 723 410" preserveAspectRatio="none" aria-hidden="true">
    <path d="M440 410 C 560 360, 640 290, 655 200 L 723 200 L 723 410 Z" fill="var(--sweep)"/>
    <path d="M472 0 C 620 40, 700 140, 655 230 C 620 310, 560 370, 462 410 L 723 410 L 723 0 Z" fill="var(--orange)"/>
  </svg>

  <div class="brand">
    <span class="brand__mark"></span>
    <span class="brand__name">Truly<br>Marvelous</span>
  </div>

  <div class="divider"></div>

  <div class="person">
    <p class="person__name">Dan Keller</p>
    <p class="person__role">CEO</p>
  </div>

  <address class="address" style="font-style:normal">
    4-8-11 Minamisato,<br>
    Hinoda-ku, Tokyo 15230
  </address>

  <ul class="contacts">
    <li>
      <svg viewBox="0 0 12 12"><path d="M3 1 L5 3.5 L4 5 Q5 7 7 8 L8.5 7 L11 9 L9.5 11 Q5 11 2.5 7 Q1 4 1.5 2 Z"/></svg>
      (021)5550192
    </li>
    <li>
      <svg viewBox="0 0 12 12"><rect x="0.5" y="2" width="11" height="8" rx="1"/><path d="M1 2.5 L6 6.5 L11 2.5" stroke="#fff" stroke-width="1" fill="none"/></svg>
      dan@marvelous.com
    </li>
    <li>
      <svg viewBox="0 0 12 12"><circle cx="6" cy="6" r="5.5"/><path d="M0.5 6 H11.5 M6 0.5 V11.5" stroke="#fff" stroke-width="0.8"/></svg>
      www.trulymarvelous.com
    </li>
  </ul>
</section>

<section class="card card--back">
  <div class="brand">
    <span class="brand__mark"></span>
    <span class="brand__name">Truly<br>Marvelous</span>
  </div>
</section>

</body>
</html>
```